Cannabis Media Network Advertising Kit

Northpine Herbal Channel is a digital media news network focused on the startups, entrepreneurs and innovative companies in the cannabis industry. We are ready to release our new services for 2017.

We are looking for a modern looking advertising kit created that we would send to our potential clients.

We want it to look similar to our branding. Our website is www.northpineherbalchannel.com.

Target Market(s)

Page 3: Audience:
Entrepreneurs, professionals, execs, VC’s, and Investors
Include stats: 34% Female/ 66% Male, 34% 25-34 Years Old $24% 35-44 Years Old

Industry/Entity Type

Media

Font styles to use
Sans Serif

Colors
0555a3
0492cd
ffffff
edf1f7

Requirements
Must have
• Outline Idea is below. Images can be provided.
• Page 1: Header Page (NHC logo)
• Leading digital media news network covering the latest tech, startups, and innovative companies in the cannabis industry.
• Page 2: About Us - Mission and Brand
• Northpine Herbal Channel is the leading digital media platform that is dedicated to profiling the startups, entrepreneurs and innovative companies in the cannabis industry.
• Over the past few years we have been highlighting the upcoming and established businesses in the industry, developed a platform for leaders to share their knowledge and insight, and created
• a spotlight for the innovative technology.
• But most importantly, we have created a community of entrepreneurs, investors and professionals who have the same mission of growing the b2b industry together.
• NHC is more than just a network and brand, we are highlighting history in the making of high quality original content.
• Page 3: Audience:
• Entrepreneurs, professionals, execs, VC’s, and Investors
• Include stats: 34% Female/ 66% Male, 34% 25-34 Years Old $24% 35-44 Years Old
• Page 4: NHC Original Web Series
• Pre/Post Commercial Opportunities $5,000
• Lantern Critiques and NHC Chats
• Lantern Critiques is a un-biased product review segment for the wholesalers, online stores, dispensaries and more.
• NHC Chats: One on one interview with the upcoming and leading founders offering advice and insight for fellow entrepreneurs.
• Page 5: NHC Original Web Series
• Biscuits and Botanicals is a female founder focused web series, where we highlight the leaders, discuss informative topics and latest products.
• Product placement $2,500
• Page 6: NHC Original Web Series
• Ledger Lane gives you a peek into the entrepreneur 2.0 and what it is like running a cannabis business.
• See leadership package
• Page 7: Package 1: Foundation $1,000
• 1. Four full platform ads (via QP, VM, Chirplo, Workverse, Snipboard)
• 2. NHC Article/Company Spotlight (One Newsletter feature and full NHC promotion)
• 3. Newsletter Ad (One run, assets provided by client
• Page 8: Package 2: Traction $5,000
• 1. Six full platform ads (via QP, VM, Chirplo, Workverse, Snipboard)
• 4. Business of the Month Badge (NHC Homepage)
• 5. Three Verbal Video Advertisements ( Three segments, up to 10 seconds each)
• Page 9: Package 3: Leadership $15,000
• 5. Three Video Advertisements (Three segments, 30 second commercial)
• 7. Ledger Lane Full Segment
• Includes promo and full segment promoted and released via NHC.
• Page 10: Events Promotion
• Event Package $1,000
• 1. Four full platform ads (via QP include QP Event on NHC Page, VM, Chirplo, Workverse, Snipboard)
• A la Carte:
• Add event to NHC calendar, basic promotion via social media $250
• NHCTV Media Sponsor
• Includes co-branded video production of event, exclusive interview with sponsors, and more
• *Cost: To Be Determined
• Page 11: A La Carte
• 1. Event Addition to Calendar (Basic promotion via social media)
• 2. Six full platform ads (via QP, VM, Chirplo, Workverse, Snipboard)
• 3. NHC Article/Company Spotlight (One Newsletter feature and full NHC promotion)
• 4. Newsletter Ad (One run, assets provided by client
• 5. Business of the Month Badge (NHC Homepage)
• 6. Three Verbal Video Advertisements ( Three segments, up to 10 seconds each)
• Page 12: Traction
• Profiled on workverse, pear bulletin, swivelpage, quillpage, chirplo, vistamoment
• 10k+ organic email list of professionals
• 16k+ page views increasing 25% each month
• 18k+ social media followers
• Viewed in all 50 states and 98 countries
• Page 13: Message from the CEO
• “We at NHC understand that our industry is different than any other industry out there, we even look at the entrepreneurs and don’t see them just as an entrepreneur but as an entrepreneur 2.0. Why? Because this is the first time in a long time where we have the opportunity to change how an industry is built from the foundation up and each of these individuals are faced with hurdles and challenges we wouldn’t face in any other industry and yet they are doing what it takes to continue to move forward.”
• Page 14: Contact Us
• NHC logo:
• We look forward to growing your brand with the Northpine Herbal Channel! Contact us today at contact@northpineherbalchannel.com
Nice to have
• High Res Images from our content. Which we can provide those images, or you can pull from our site and we can send high res after.
Should not have
• Dark Designed.

```html
<!DOCTYPE html>
<html lang="en">
<head>
<meta charset="UTF-8">
<title>Northpine Herbal Channel — Advertising Kit 2017</title>
<link rel="stylesheet" href="https://fonts.googleapis.com/css2?family=Arimo:wght@700&family=Montserrat:wght@300&display=swap">
<style>
  :root {
    --page-bg: #ffffff;
    --royal-blue: #0a47f0;
    --sky-blue: #38b2f5;
    --rule-blue: #3aa6f2;
    --white: #ffffff;
    --name-tint: #e9eef5;
  }
  * { margin: 0; padding: 0; box-sizing: border-box; }
  html, body {
    width: 1200px;
    height: 1200px;
    overflow: hidden;
    background: var(--page-bg);
  }
  .canvas {
    position: relative;
    width: 1200px;
    height: 1200px;
    background: var(--page-bg);
  }
  .cover {
    position: absolute;
    left: 149px;
    top: 0;
    width: 901px;
    height: 1200px;
    overflow: hidden;
    background: var(--royal-blue);
  }
  .cover-split {
    position: absolute;
    inset: 0;
    width: 901px;
    height: 1200px;
  }
  .tagline {
    position: absolute;
    left: 57px;
    top: 58px;
    display: flex;
    align-items: center;
    gap: 9px;
  }
  .tagline-mark {
    width: 22px;
    height: 22px;
    background: var(--sky-blue);
  }
  .tagline-text {
    font-family: "Arimo", Arial, sans-serif;
    font-weight: 700;
    font-size: 14.6px;
    letter-spacing: -0.6px;
    color: var(--white);
    white-space: nowrap;
  }
  .rule {
    position: absolute;
    left: 0;
    height: 4px;
    background: var(--rule-blue);
  }
  .rule-one { top: 112px; width: 677px; }
  .rule-two { top: 124px; width: 798px; }
  .rule-three { top: 135px; width: 405px; }
  .brand-name {
    position: absolute;
    left: 555px;
    top: 772px;
    font-family: "Montserrat", "Helvetica Neue", sans-serif;
    font-weight: 300;
    font-size: 40px;
    line-height: 63px;
    letter-spacing: 8px;
    color: var(--name-tint);
    text-transform: uppercase;
  }
  .brand-dot {
    position: absolute;
    left: 505px;
    top: 798px;
    width: 26px;
    height: 26px;
    border-radius: 50%;
    background: var(--white);
  }
  .issue {
    position: absolute;
    left: 0;
    right: 0;
    top: 1114px;
    display: flex;
    justify-content: center;
    align-items: center;
    gap: 10px;
    padding-left: 2px;
  }
  .issue-line {
    width: 64px;
    height: 3px;
    background: var(--white);
  }
  .issue-label {
    font-family: "Arimo", Arial, sans-serif;
    font-weight: 700;
    font-size: 20px;
    color: var(--white);
  }
</style>
</head>
<body>
<main class="canvas">
  <section class="cover">
    <svg class="cover-split" viewBox="0 0 901 1200" aria-hidden="true">
      <polygon points="899,0 901,0 901,1200 235,1200" fill="var(--sky-blue)"/>
    </svg>

    <header class="tagline">
      <span class="tagline-mark"></span>
      <p class="tagline-text">Leading digital media news network covering the latest tech, startups,and&nbsp; innovative companies in the cannabis industry.</p>
    </header>

    <div class="rule rule-one"></div>
    <div class="rule rule-two"></div>
    <div class="rule rule-three"></div>

    <span class="brand-dot"></span>
    <h1 class="brand-name">Northpine<br>Herbal<br>Channel</h1>

    <footer class="issue">
      <span class="issue-line"></span>
      <span class="issue-label">issue 2017</span>
      <span class="issue-line"></span>
    </footer>
  </section>
</main>
</body>
</html>
```